Business Card Design

I am a GP with interest in Dermatology and Aesthetic Medicin, performing Botulinum Toxin Type A and Dermal Fillers treatmets in Cosmetic Dermatology clinic.

I am looking for a white colour, good quality white paper card may be of some special texture with black calligraphic writing but easy to read and not to wiggly- professional- looking.

Really appreciate your help.

Halyna

Cosmetic Dermatology Clinic

Dr Halyna Korbutiak, MBBS, MRCGP, DPD

Tel: 07841 615 092
halyna@medmailbox.org.uk

```html
<!DOCTYPE html>
<html lang="en">
<head>
<meta charset="utf-8">
<title>Cosmetic Dermatology Clinic – Business Card</title>
<link rel="stylesheet" href="https://fonts.googleapis.com/css2?family=Yellowtail&family=Didact+Gothic&display=swap">
<style>
  :root {
    --paper: #ffffff;
    --accent: #e81fdc;
    --ornament: #d94ff0;
    --ink: #141414;
    --rule: #333333;
  }
  html, body {
    margin: 0;
    padding: 0;
    overflow: hidden;
    background: var(--paper);
  }
  .card {
    position: relative;
    width: 1200px;
    height: 731px;
    background: var(--paper);
    overflow: hidden;
  }
  .frame-lines {
    position: absolute;
    inset: 0;
  }
  .corner-ornament {
    position: absolute;
  }
  .corner-ornament--top-left {
    left: 39px;
    top: 50px;
    width: 278px;
    height: 264px;
  }
  .corner-ornament--bottom-right {
    left: 876px;
    top: 411px;
    width: 277px;
    height: 263px;
  }
  .clinic-name,
  .doctor-name {
    position: absolute;
    left: 0;
    width: 1194px;
    margin: 0;
    text-align: center;
    font-family: "Yellowtail", cursive;
    font-weight: 400;
    color: var(--accent);
    line-height: 1;
  }
  .clinic-name {
    top: 170px;
    font-size: 52px;
    word-spacing: 8px;
  }
  .doctor-name {
    top: 253px;
    font-size: 52px;
  }
  .qualifications {
    position: absolute;
    left: 534px;
    top: 347px;
    margin: 0;
    padding: 0;
    list-style: none;
    font-family: "Didact Gothic", sans-serif;
    font-size: 31px;
    color: var(--ink);
    letter-spacing: -1.5px;
  }
  .qualifications li {
    position: relative;
    height: 44.5px;
    line-height: 44.5px;
    padding-left: 34px;
  }
  .qualifications li::before {
    content: "";
    position: absolute;
    left: 0;
    top: 14px;
    width: 13px;
    height: 13px;
    background: var(--accent);
  }
  .contact {
    position: absolute;
    left: 72px;
    top: 558px;
    margin: 0;
    font-family: "Yellowtail", cursive;
    font-size: 38px;
    line-height: 42px;
    color: var(--accent);
    font-style: normal;
    letter-spacing: 1px;
  }
  .contact span {
    display: block;
  }
</style>
</head>
<body>
  <div class="card">
    <svg class="frame-lines" width="1200" height="731" viewBox="0 0 1200 731" aria-hidden="true">
      <g fill="none" stroke="var(--rule)" stroke-width="2.2" stroke-dasharray="2 2.5">
        <polyline points="356,51 1152,51 1152,376"/>
        <polyline points="40,370 40,673 822,673"/>
      </g>
    </svg>

    <svg class="corner-ornament corner-ornament--top-left" viewBox="0 0 278 264" role="img" aria-label="Decorative floral scroll corner ornament">
      <polygon points="0,0 278,0 0,264" fill="var(--ornament)"/>
    </svg>

    <svg class="corner-ornament corner-ornament--bottom-right" viewBox="0 0 277 263" role="img" aria-label="Decorative floral scroll corner ornament">
      <polygon points="277,0 277,263 0,263" fill="var(--ornament)"/>
    </svg>

    <h1 class="clinic-name">Clinic&nbsp; Cosmetic Dermatology</h1>
    <h2 class="doctor-name">Dr Halyna Korbutiak</h2>

    <ul class="qualifications">
      <li>MBBS</li>
      <li>MRCGP</li>
      <li>DPD</li>
    </ul>

    <address class="contact">
      <span class="contact__phone">Tel: 07841 615 092</span>
      <span class="contact__email">halyna@medmailbox.org.uk</span>
    </address>
  </div>
</body>
</html>
```